New Business cards design and layout
Verant cards
New Business cards design and layout - Information Technology
Creative Brief
Professional
Dorian T. Halvek
VP, Sales and Business Development
4718 - 12th Avenue N.W. Calgary, Alberta T3K 1R8
dorian@verantinfo.ca
www.verantinfo.ca

```html
<!DOCTYPE html>
<html lang="en">
<head>
<meta charset="utf-8">
<title>Verant business cards</title>
<link href="https://fonts.googleapis.com/css2?family=Montserrat:wght@400;500;700;800&display=swap" rel="stylesheet">
<style>
  :root {
    --backdrop: #e4e4e2;
    --card: #f7f7f6;
    --brand-blue: #1f63c6;
    --ink: #2b3240;
    --muted: #6b7280;
    --shadow: rgba(20, 24, 32, 0.22);
  }
  * { box-sizing: border-box; margin: 0; padding: 0; }
  html, body {
    width: 1200px; height: 899px; overflow: hidden;
    background: var(--backdrop);
    font-family: "Montserrat", sans-serif;
  }
  .stage {
    width: 1200px; height: 899px;
    display: flex; align-items: center; justify-content: center; gap: 48px;
  }
  .card {
    position: relative;
    width: 540px; height: 309px;
    background: var(--card);
    border-radius: 26px;
    box-shadow: 0 18px 40px var(--shadow);
  }
  /* front: contact side */
  .contact-grid {
    position: absolute; top: 42px; right: 36px;
    display: grid; grid-template-columns: auto auto;
    column-gap: 30px; row-gap: 22px;
  }
  .contact-item { display: flex; align-items: flex-start; gap: 10px; }
  .contact-icon {
    flex: none; width: 22px; height: 22px; border-radius: 5px;
    background: var(--brand-blue);
    display: flex; align-items: center; justify-content: center;
  }
  .contact-icon svg { width: 13px; height: 13px; }
  .contact-text {
    font-size: 10.5px; line-height: 1.45; color: var(--muted); font-weight: 500;
  }
  .holder { position: absolute; left: 40px; bottom: 44px; }
  .holder-name {
    font-size: 17px; font-weight: 800; color: var(--ink);
    letter-spacing: 0.04em; text-transform: uppercase;
  }
  .holder-title {
    margin-top: 4px; font-size: 9.5px; color: var(--muted);
    letter-spacing: 0.08em; text-transform: uppercase; font-weight: 500;
  }
  /* back: brand side */
  .brand {
    position: absolute; inset: 0;
    display: flex; align-items: center; justify-content: center; gap: 16px;
  }
  .brand-dot {
    width: 46px; height: 46px; border-radius: 50%; background: var(--brand-blue);
  }
  .brand-name {
    font-size: 58px; font-weight: 800; color: var(--brand-blue);
    letter-spacing: 0.06em; text-transform: uppercase;
  }
</style>
</head>
<body>
<main class="stage">
  <section class="card card-front" aria-label="Card front with contact details">
    <div class="contact-grid">
      <div class="contact-item">
        <span class="contact-icon">
          <svg viewBox="0 0 24 24" fill="#fff"><path d="M6.6 10.8a15.1 15.1 0 0 0 6.6 6.6l2.2-2.2a1 1 0 0 1 1-.25 11.4 11.4 0 0 0 3.6.57 1 1 0 0 1 1 1V20a1 1 0 0 1-1 1A17 17 0 0 1 3 4a1 1 0 0 1 1-1h3.5a1 1 0 0 1 1 1c0 1.25.2 2.45.57 3.6a1 1 0 0 1-.25 1z"/></svg>
        </span>
        <p class="contact-text">403 555 0182<br>403 555 0183</p>
      </div>
      <div class="contact-item">
        <span class="contact-icon">
          <svg viewBox="0 0 24 24" fill="none" stroke="#fff" stroke-width="2"><circle cx="12" cy="12" r="9"/><path d="M3 12h18M12 3c3 3.5 3 14.5 0 18M12 3c-3 3.5-3 14.5 0 18"/></svg>
        </span>
        <p class="contact-text">www.verantinfo.ca</p>
      </div>
      <div class="contact-item">
        <span class="contact-icon">
          <svg viewBox="0 0 24 24" fill="none" stroke="#fff" stroke-width="2"><rect x="3" y="5" width="18" height="14" rx="1"/><path d="M3 6l9 7 9-7"/></svg>
        </span>
        <p class="contact-text">dorian@verantinfo.ca</p>
      </div>
      <div class="contact-item">
        <span class="contact-icon">
          <svg viewBox="0 0 24 24" fill="#fff"><path d="M12 2a7 7 0 0 0-7 7c0 5 7 13 7 13s7-8 7-13a7 7 0 0 0-7-7zm0 9.5A2.5 2.5 0 1 1 12 6.5a2.5 2.5 0 0 1 0 5z"/></svg>
        </span>
        <p class="contact-text">4718 - 12th Avenue N.W.<br>Calgary, Alberta<br>T3K 1R8</p>
      </div>
    </div>
    <div class="holder">
      <h1 class="holder-name">Dorian T. Halvek</h1>
      <p class="holder-title">VP, Sales and Business Development</p>
    </div>
  </section>

  <section class="card card-back" aria-label="Card back with company name">
    <div class="brand">
      <span class="brand-dot"></span>
      <span class="brand-name">Verant</span>
    </div>
  </section>
</main>
</body>
</html>
```